Profile Card Layout/Design Template

We recently ran a workshop with a client and during that workshop we developed some typical profiles of their target audience using flip chart paper. We now want to turn the profiles into professionally designed A5 cards we can then print and give to the client, therefore we require the profile card layout template to be designed so that in the future we can insert the profile data and images in-house.
Attached are 3 files.
1. persona_gretaplume.jpg is one of profiles we want to convert
2. profilecards.png is an example of the type of design/layout we need to convert the flip chart data to.
3. our company logo
So the layout needs to provide space for
- the profile data specified in persona_gretaplume.jpg
- some additional space for a profile summary/overview not currently shown in persona_gretaplume.jpg but
- an image/photo of the profiled person
- a placeholder for the clients logo
- a placeholder for our company logo
- placeholders for appropriate images to compliment the profile
Happy to consider both portrait and landscape designs
Would be good but not essential if we could change colours of specific elements of the design to compliment the clients corporate colours. So for instance our current clients corporate colours are #b50700, #001739 & #000000

```html
<!DOCTYPE html>
<html lang="en">
<head>
<meta charset="utf-8">
<title>Greta Plume – Profile Card</title>
<link rel="stylesheet" href="https://fonts.googleapis.com/css2?family=Anton&family=Archivo+Narrow:wght@400&family=Carlito:ital,wght@0,700;1,700&family=Montserrat:wght@600;700&family=Pathway+Gothic+One&display=swap">
<style>
  :root {
    --page-bg: #2b2b2b;
    --brand-green: #a8cf3a;
    --brand-yellow: #f6ea14;
    --cream-top: #fffef0;
    --cream-bottom: #fbf7cf;
    --ink: #111111;
    --panel-white: #ffffff;
    --panel-border: #8c8c8c;
    --band-black: #000000;
    --on-dark: #ffffff;
  }
  * { box-sizing: border-box; margin: 0; padding: 0; }
  html, body { width: 1200px; height: 900px; overflow: hidden; }
  body { background: var(--page-bg); position: relative; }

  .profile-card {
    position: absolute; left: 60px; top: 73px;
    width: 863px; height: 603px;
    transform: scale(1.25); transform-origin: 0 0;
    background: linear-gradient(180deg, var(--cream-top) 0%, var(--cream-bottom) 100%);
    overflow: hidden; color: var(--ink);
  }
  .header-band { position: absolute; left: 0; top: 0; width: 863px; height: 83px; background: var(--brand-green); }
  .header-stripe { position: absolute; left: 0; top: 83px; width: 863px; height: 12px; background: var(--brand-yellow); }
  .footer-band { position: absolute; left: 0; top: 585px; width: 863px; height: 18px; background: var(--brand-green); }

  .persona-name {
    position: absolute; left: 37px; top: 22px;
    font: italic 700 60px/1 "Carlito", sans-serif; letter-spacing: -0.5px;
    text-shadow: 2px 0 #fff, -2px 0 #fff, 0 2px #fff, 0 -2px #fff, 1.5px 1.5px #fff, -1.5px -1.5px #fff, 1.5px -1.5px #fff, -1.5px 1.5px #fff;
  }

  .goal-badge { position: absolute; left: 118px; top: 122px; width: 156px; height: 62px; }
  .goal-badge svg { position: absolute; inset: 0; }
  .goal-label {
    position: absolute; left: 0; top: 12px; width: 100%; text-align: center;
    font: 400 27px/1 "Anton", sans-serif; letter-spacing: 0.5px;
  }
  .goal-text {
    position: absolute; left: 10px; top: 187px; width: 370px; text-align: center;
    font: italic 700 21px/29px "Carlito", sans-serif;
  }

  .trait-column { position: absolute; top: 264px; font-family: "Pathway Gothic One", sans-serif; }
  .trait-column--left { left: 28px; }
  .trait-column--right { left: 205px; }
  .trait-heading { font-size: 12.5px; line-height: 16px; text-decoration: underline; text-transform: uppercase; }
  .trait-list { list-style: none; font-size: 11px; line-height: 16.2px; margin-bottom: 8px; }

  .maker-credit { position: absolute; left: 30px; top: 469px; display: flex; align-items: center; gap: 7px; }
  .maker-mark { width: 12px; height: 12px; background: var(--brand-green); }
  .maker-text { font-family: "Montserrat", sans-serif; font-weight: 700; line-height: 1.3; }
  .maker-text .small { font-size: 6.6px; letter-spacing: 1.4px; }
  .maker-text .name { font-size: 8px; letter-spacing: 3px; }

  .client-logo-slot {
    position: absolute; left: 233px; top: 466px; width: 116px; height: 26px;
    background: var(--band-black); color: var(--on-dark);
    font: 700 9px/26px "Montserrat", sans-serif; text-align: center; letter-spacing: 0.3px;
  }

  .profile-panel {
    position: absolute; left: 405px; top: 20px; width: 440px; height: 473px;
    background: var(--panel-white); border: 3px solid var(--panel-border); border-radius: 9px;
  }
  .name-tab {
    position: absolute; left: 405px; top: 20px; width: 212px; height: 93px;
    background: var(--panel-white); border: 3px solid var(--panel-border); border-radius: 9px 0 0 0;
    font: italic 700 24px/80px "Carlito", sans-serif; text-align: center; font-weight: 400;
  }
  .photo-frame {
    position: absolute; left: 611px; top: 13px; width: 240px; height: 250px;
    background: var(--panel-white); border: 3px solid var(--panel-border); border-radius: 9px;
    transform: rotate(0.6deg);
    font: italic 400 24px/1 "Carlito", sans-serif;
    display: flex; align-items: center; justify-content: center; padding-bottom: 10px;
  }
  .profile-summary {
    position: absolute; left: 429px; top: 133px;
    font: 400 10.2px/17.3px "Archivo Narrow", sans-serif; white-space: nowrap;
  }

  .image-strip {
    position: absolute; left: 15px; top: 501px; width: 833px; height: 78px;
    background: var(--band-black); color: var(--on-dark);
    font: 600 12.5px/78px "Montserrat", sans-serif; text-align: center;
  }
</style>
</head>
<body>
  <div class="profile-card">
    <div class="header-band"></div>
    <div class="header-stripe"></div>
    <div class="footer-band"></div>

    <h1 class="persona-name">Greta Plume</h1>

    <div class="goal-badge">
      <svg viewBox="0 0 156 62" width="156" height="62" aria-hidden="true">
        <ellipse cx="78" cy="31" rx="72" ry="25" fill="#ffffff" stroke="var(--brand-yellow)" stroke-width="7"/>
      </svg>
      <div class="goal-label">GOAL:</div>
    </div>
    <p class="goal-text">Have Fun Being Physically Active Like Minded People.</p>

    <div class="trait-column trait-column--left">
      <h2 class="trait-heading">What Motivates Me?</h2>
      <ul class="trait-list">
        <li>- Friendship/Relationship</li>
        <li>- Making The Most Of ___?</li>
        <li>- Value For Money</li>
        <li>- Fun Environment</li>
        <li>- Well Organized</li>
      </ul>
      <h2 class="trait-heading">Behavior</h2>
      <ul class="trait-list">
        <li>- Busy</li>
        <li>- No Flashy Technology</li>
      </ul>
    </div>

    <div class="trait-column trait-column--right">
      <h2 class="trait-heading">Frustration/Fear/Concerns</h2>
      <ul class="trait-list">
        <li>- Doesn't Like Down Time</li>
        <li>- Wasting My Time</li>
        <li>- Who's Looking After The Bids</li>
        <li>- I Won't Be Able To Play</li>
      </ul>
      <h2 class="trait-heading">Pair Points</h2>
      <ul class="trait-list">
        <li>- Things Must Just Work - Functional</li>
        <li>- You Won't Be Good Enough</li>
        <li>- Scared Of Being Hurt</li>
        <li>- No Hit</li>
        <li>- Knowledge Of Rules</li>
      </ul>
    </div>

    <div class="maker-credit">
      <span class="maker-mark"></span>
      <div class="maker-text">
        <div class="small">DESIGNED AND POWERED BY</div>
        <div class="name">BRIGHT FORGE</div>
      </div>
    </div>
    <div class="client-logo-slot" role="img" aria-label="Client logo placeholder">CLIENTS LOGO</div>

    <div class="profile-panel"></div>
    <div class="name-tab">Name</div>
    <div class="photo-frame" role="img" aria-label="Photo of the profiled person">PHOTO</div>

    <div class="profile-summary">
      PROFILE: Lorem ipsum dolor sit amet,<br>
      consetetur sadipscing elitr,&nbsp; sed diam<br>
      nonumy eirmod tempor invidunt ut<br>
      labore et dolore magna aliquyam erat,<br>
      sed diam voluptua. At vero eos et<br>
      accusam et justo duo dolores et ea<br>
      rebum. Stet clita kasd gubergren, no sea<br>
      takimata sanctus est Lorem ipsum dolor.<br>
      Lorem ipsum dolor sit amet, consetetur sadipscing elitr,&nbsp; sed diam nonumy eirmod tempor<br>
      invidunt ut labore et dolore magna aliquyam erat, sed diam voluptua. At vero eos et accusam et<br>
      justo duo dolores et ea rebum. Stet clita kasd gubergren, no sea takimata sanctus est Lorem<br>
      ipsum dolor sit amet. Lorem ipsum dolor sit amet, consetetur sadipscing elitr,&nbsp; sed diam nonumy<br>
      eirmod tempor invidunt ut labore et dolore magna aliquyam erat, sed diam voluptua. At vero<br>
      eos et accusam et justo duo dolores et ea rebum. Stet clita kasd gubergren, no sea takimata<br>
      sanctus est Lorem ipsum dolor sit amet. Lorem ipsum dolor sit amet, consetetur sadipscing elitr,<br>
      sed diam nonumy eirmod tempor invidunt ut labore et dolore magna aliquyam erat, sed diam<br>
      voluptua. At vero eos et accusam et justo duo dolores et ea rebum. dolores et ea rebum. Stet<br>
      clita kasd gubergren, no sea takimata sanctus est Lorem ipsum dolor sit amet.<br>
      sadipscing elitr,&nbsp; sed diam nonumy eirmod tempor invidunt ut labore et dolore magna aliquyam<br>
      erat, sed diam voluptua.
    </div>

    <div class="image-strip" role="img" aria-label="Images complementing the profile">placeholders for appropriate images to compliment the profile</div>
  </div>
</body>
</html>
```